Letterhead Design Project

We are looking for a simple letterhead design that reflects our core purpose. We help our clients gain clarity and focus but we are there to help them execute. The letterhead design would mainly be utilised for engagement letters and contracts.

Target Market(s)

The customers of our business are large corporate organisations.

Requirements
Must have
• The letterhead must have the company logo
The font used must tie in to the font used in the company logo

Must have the following business details
Address: Level 10, 27 Brimley Lane, Melbourne, Australia, 3000
Phone: +61 3 502 847 193
Fax: +61 3 9412 5037
Website: www.vorndex.com.au
Twiiter: @vorndex

```html
<!DOCTYPE html>
<html lang="en">
<head>
<meta charset="utf-8">
<title>Vorndex Letterhead</title>
<link href="https://fonts.googleapis.com/css2?family=Open+Sans:wght@400&display=swap" rel="stylesheet">
<style>
  :root {
    --brand-blue: #0a4cf0;
    --band-grey: #4a4a4a;
    --paper: #ffffff;
    --backdrop: #e4e4e4;
    --ink: #222222;
    --watermark: #f1f4fc;
  }
  * { margin: 0; padding: 0; box-sizing: border-box; }
  html, body {
    width: 927px;
    height: 1200px;
    overflow: hidden;
    background: var(--backdrop);
    font-family: "Open Sans", sans-serif;
  }
  .letterhead {
    position: absolute;
    left: 53px;
    top: 100px;
    width: 812px;
    height: 1053px;
    background: var(--paper);
    overflow: hidden;
  }
  .header-swoosh {
    position: absolute;
    left: 0;
    top: 0;
    width: 812px;
    height: 280px;
  }
  .swoosh-blue { fill: var(--brand-blue); }
  .swoosh-grey { fill: var(--band-grey); }
  .brand {
    position: absolute;
    left: 40px;
    top: 52px;
    display: flex;
    align-items: center;
    gap: 14px;
  }
  .brand-name {
    font-size: 58px;
    font-weight: 400;
    color: var(--brand-blue);
    line-height: 1;
    letter-spacing: 1px;
  }
  .brand-dot {
    width: 50px;
    height: 50px;
    border-radius: 50%;
    background: var(--brand-blue);
  }
  .address {
    position: absolute;
    right: 45px;
    top: 43px;
    text-align: right;
    color: #ffffff;
    font-size: 14px;
    line-height: 19px;
    font-style: normal;
  }
  .watermark-disc {
    position: absolute;
    left: 234px;
    top: 497px;
    width: 340px;
    height: 340px;
    border-radius: 50%;
    background: var(--watermark);
  }
  .contact-bar {
    position: absolute;
    left: 0;
    right: 0;
    top: 1013px;
    display: flex;
    justify-content: center;
    gap: 16px;
    font-size: 14px;
    color: var(--ink);
    list-style: none;
  }
  .contact-item {
    display: flex;
    align-items: center;
    gap: 5px;
    white-space: nowrap;
  }
  .contact-icon { width: 12px; height: 12px; }
  .contact-icon path, .contact-icon circle, .contact-icon rect { fill: none; stroke: var(--ink); stroke-width: 1.4; }
  .social-square {
    width: 12px;
    height: 12px;
    background: #5fc3e8;
    border-radius: 2px;
  }
</style>
</head>
<body>
  <main class="letterhead">
    <svg class="header-swoosh" viewBox="0 0 812 280" aria-hidden="true">
      <path class="swoosh-grey" d="M0,0 C560,40 790,130 812,272 L812,226 C770,140 560,50 0,0 Z"/>
      <path class="swoosh-blue" d="M0,0 H812 V212 C760,125 560,42 0,0 Z"/>
    </svg>

    <div class="brand">
      <span class="brand-name">Vorndex</span>
      <span class="brand-dot" aria-hidden="true"></span>
    </div>

    <address class="address">
      Level 10, 27 Brimley Lane<br>
      Melbourne<br>
      Australia, 3000
    </address>

    <div class="watermark-disc" aria-hidden="true"></div>

    <ul class="contact-bar">
      <li class="contact-item">
        <svg class="contact-icon" viewBox="0 0 14 14" aria-hidden="true"><path d="M3,1 L5,4 L4,6 C5,8 6,9 8,10 L10,9 L13,11 L11,13 C6,13 1,8 1,3 Z"/></svg>
        +61 3 502 847 193
      </li>
      <li class="contact-item">
        <svg class="contact-icon" viewBox="0 0 14 14" aria-hidden="true"><rect x="1" y="5" width="12" height="7" rx="1"/><path d="M4,5 V1 H10 V5"/></svg>
        +61 3 9412 5037
      </li>
      <li class="contact-item">
        <svg class="contact-icon" viewBox="0 0 14 14" aria-hidden="true"><circle cx="7" cy="7" r="6"/><path d="M1,7 H13 M7,1 C3,5 3,9 7,13 M7,1 C11,5 11,9 7,13"/></svg>
        www.vorndex.com.au
      </li>
      <li class="contact-item">
        <span class="social-square" aria-hidden="true"></span>
        @vorndex
      </li>
    </ul>
  </main>
</body>
</html>
```